we need a design for Water Bottle Lable Wrap
The product is called Corvane Water is a restructured water. its a very healthy and rejuvenating water
we were looking at using as a tag ling Restore, Recover, Rejuvenate.

```html
<!DOCTYPE html>
<html lang="en">
<head>
<meta charset="utf-8">
<title>Corvane Water – Bottle Label Wrap</title>
<link rel="stylesheet" href="https://fonts.googleapis.com/css2?family=Questrial&family=Barlow+Condensed:wght@600&display=swap">
<style>
  :root {
    --page: #ffffff;
    --blue-deep: #0a4fe6;
    --blue-mid: #0f7cf0;
    --blue-bright: #2bb6f7;
    --blue-light: #9fe0ff;
    --navy: #123463;
    --white: #ffffff;
  }
  * { margin: 0; padding: 0; box-sizing: border-box; }
  html, body {
    width: 1200px;
    height: 900px;
    overflow: hidden;
    background: var(--page);
  }
  .label {
    position: absolute;
    left: 320px;
    top: 95px;
    width: 560px;
    height: 710px;
    overflow: hidden;
    background:
      linear-gradient(180deg, var(--blue-bright) 0%, var(--blue-mid) 55%, var(--blue-deep) 100%);
    font-family: "Questrial", sans-serif;
    color: var(--white);
  }
  .water-splash {
    position: absolute;
    left: 0;
    top: 0;
    width: 560px;
    height: 400px;
    background:
      radial-gradient(ellipse 60% 40% at 70% 40%, rgba(220,245,255,0.85) 0%, rgba(159,224,255,0.45) 45%, rgba(43,182,247,0) 80%),
      radial-gradient(ellipse 50% 30% at 30% 20%, rgba(180,235,255,0.55) 0%, rgba(43,182,247,0) 75%);
  }
  .brand-name {
    position: absolute;
    left: 0;
    width: 100%;
    top: 325px;
    text-align: center;
    font-size: 96px;
    line-height: 1;
    letter-spacing: -1px;
    color: var(--white);
  }
  .tagline {
    position: absolute;
    left: 0;
    width: 100%;
    top: 460px;
    text-align: center;
    font-family: "Barlow Condensed", sans-serif;
    font-weight: 600;
    font-size: 27px;
    letter-spacing: 0.3px;
    color: var(--navy);
  }
  .product-type {
    position: absolute;
    left: 0;
    width: 100%;
    top: 592px;
    text-align: center;
    font-size: 19px;
  }
  .product-rule {
    position: absolute;
    left: 190px;
    top: 622px;
    width: 190px;
    height: 1.5px;
    background: var(--white);
  }
  .volume {
    position: absolute;
    left: 0;
    width: 100%;
    top: 637px;
    text-align: center;
    font-size: 18px;
  }
</style>
</head>
<body>
  <main class="label">
    <div class="water-splash" role="img" aria-label="Illustration of a flowing water splash with bubbles"></div>
    <h1 class="brand-name">corvane</h1>
    <p class="tagline">RESTORE · RECOVER · REJUVENATE</p>
    <p class="product-type">Restructured Water</p>
    <div class="product-rule"></div>
    <p class="volume">500mL</p>
  </main>
</body>
</html>
```